Broschüre für Immobilienvertrieb
Zielgruppe
Wir sind ein Immobilienvertrieb im Bereich Neubau-Immobilien und Bestand-Immobilien aus München. Die Firma BLOR existiert seit über 30 Jahren. Vor 4 Jahren haben wir ein cooles modernes Rebranding durchgeführt, sodass man mit unserem neuen Corporate Design richtig Spaß am Gestalten haben kann.
Eine konkrete Zielgruppe zu definieren ist schwierig, da unsere Käufer von 20-80 Jahren sein können. Ob junge, erfolgreiche Menschen, junge Familien, ältere Erwachsene, die von sich nach Auszug ihrer Kinder von ihrem Haus trennen wollen und eine kleinere Wohnung suchen oder einfach der Kapitalanleger, der auf der Suche nach einer neuen Investition ist.
Unsere CI ist gradlinig und setzt sich aus anthrazit, neonorange und weiß zusammen (Styleguide ist anbei).
Im Bestand gibt es nicht pro Objekt ein CI, hier wird mit dem der BLOR gearbeitet. Im Neubau hat jedes einzelne Projekt sein eigenes CI (siehe aktuell hausfeld-neu.de).
www.blor.de
Aufgabenstellung
Zur Aufgabe: Für die Bestandimmobilien benötigen wir ein neues Layout eines Immobilienexposé. Das Exposé wird sowohl online verwendet als auch von uns selbst gedruckt und gebunden.
Input: beigefügt ein Beispielexposé - grundsätzlich gefällt uns das Design, wir möchten jedoch etwas NEUES, modernes. Bitte keine Kopien des alten Exposés, dies soll nur als Input dienen (gerne können die Daten der Wohnung für den neuen Designentwurf genutzt werden).
Die Datei soll von uns befüllbar sein, sodass wir Texte und Bilder selbst austauschen können.
Für die Onlinenutzung gerne als doppelseitige Datei, zum Beispiel um Bilder über zwei Seiten größer und schöner darstellen zu können (Auszug Beispielimmobilie anbei). Für den Druck wird die Datei zudem mit Einzelseiten benötigt.

```html
<!DOCTYPE html>
<html lang="de">
<head>
<meta charset="utf-8">
<title>BLOR Exposé</title>
<link href="https://fonts.googleapis.com/css2?family=Red+Hat+Display:wght@400;500;600;700;800&display=swap" rel="stylesheet">
<style>
:root{
  --orange:#e6512f;
  --anthracite:#2a2b2f;
  --white:#ffffff;
  --backdrop:#d2d2d2;
  --grey-line:#9a9a9a;
  --body-text:#3a3a3a;
}
*{margin:0;padding:0;box-sizing:border-box}
html,body{width:1200px;height:1200px;overflow:hidden}
body{background:var(--backdrop);font-family:"Red Hat Display",Arial,sans-serif;position:relative}
.spread{position:absolute;left:251px;width:698px;height:496px;display:flex;box-shadow:0 6px 18px rgba(0,0,0,.18)}
.spread--cover{top:70px}
.spread--inside{top:632px}
.page{position:relative;width:349px;height:496px;overflow:hidden}
.page--orange{background:var(--orange);color:var(--white)}
.page--white{background:var(--white)}

/* back cover */
.back-photo{position:absolute;inset:0;background:radial-gradient(ellipse at 55% 40%,rgba(255,255,255,.12),rgba(255,255,255,0) 60%)}
.tagline{position:absolute;left:11px;top:78px;font-size:18.5px;line-height:22.4px;font-weight:600;width:220px}
.tagline-rule{position:absolute;left:11px;top:198px;width:148px;height:3px;background:var(--white)}
.contact{position:absolute;left:11px;top:380px;font-size:6.6px;line-height:9.4px;font-weight:500}
.contact-title{font-size:11px;font-weight:700;text-decoration:underline;text-underline-offset:2px;margin-bottom:5px}
.contact b{font-weight:700}
.contact .group{margin-top:5px}
.contact .group-title{font-weight:700}
.badge{position:absolute;left:276px;top:413px}

/* front cover */
.band{position:absolute;left:0;width:100%;height:10px;background:var(--anthracite)}
.band--top{top:0}.band--bottom{bottom:0}
.brand-name{position:absolute;left:0;width:100%;top:52px;text-align:center;font-size:26px;font-weight:700;letter-spacing:6px;color:var(--anthracite)}
.bracket{position:absolute;left:299px;top:94px;width:50px;height:280px;background:var(--orange)}
.bracket-inner{position:absolute;left:299px;top:108px;width:43px;height:253px;background:var(--white)}
.cover-photo{position:absolute;left:6px;top:122px;width:319px;height:224px;background:linear-gradient(160deg,#8fa1b4 0%,#c9d0d7 45%,#b8a18a 75%,#6f6a66 100%)}
.headline{position:absolute;left:0;width:100%;top:384px;text-align:center;font-size:26px;line-height:28px;font-weight:800}
.headline .dark{color:var(--anthracite)}
.headline .accent{color:var(--orange)}
.cover-url{position:absolute;left:0;width:100%;top:460px;text-align:center;font-size:10px;letter-spacing:4.6px;color:var(--anthracite);font-weight:500}

/* inside */
.section-mark{position:absolute;left:0;width:20px;height:38px;background:var(--orange)}
.section-title{position:absolute;left:28px;font-size:16px;font-weight:700;color:var(--orange);line-height:18px}
.section-rule{position:absolute;left:28px;height:2px;background:var(--grey-line)}
.section-rule::before{content:"";position:absolute;left:0;top:0;width:20px;height:2px;background:var(--anthracite)}
.body-copy{position:absolute;left:28px;width:315px;font-size:6px;line-height:10.5px;color:var(--body-text);text-align:justify}
.feature-box{position:absolute;left:29px;top:309px;width:309px;height:177px;background:var(--orange);color:var(--white)}
.feature-col-title{position:absolute;top:7px;font-size:12px;font-weight:700;text-decoration:underline;text-underline-offset:3px}
.feature-list{position:absolute;list-style:none}
.feature-list--main{left:12px;top:33px;font-size:8px;line-height:17.7px;font-weight:500;width:118px}
.feature-list--main li::before,.feature-list--detail li::before{content:"▪ "}
.feature-list--main li.cont::before{content:"";padding-left:6px}
.feature-divider{position:absolute;left:133px;top:28px;width:1px;height:138px;background:rgba(255,255,255,.7)}
.feature-list--detail{left:145px;top:29px;width:156px;font-size:4.4px;line-height:7px;font-weight:600;text-transform:uppercase}

.project-grid{position:absolute;left:0;top:63px;width:332px;height:428px;background:var(--anthracite)}
.project{position:absolute}
.project-label{position:absolute;left:3px;top:22px;background:var(--orange);color:var(--white);font-size:7.4px;font-weight:700;padding:3px 4px;text-transform:uppercase;white-space:nowrap}
.p1{left:2.5px;top:4px;width:160px;height:250px;background:linear-gradient(180deg,#b9c4cf 0%,#dcdcd8 40%,#9aa08f 70%,#d8cdb8 100%)}
.p2{left:165px;top:4px;width:164px;height:168px;background:linear-gradient(180deg,#4a6a96 0%,#8fa3be 40%,#d9d6d0 65%,#3f4a3e 100%)}
.p3{left:2.5px;top:256px;width:160px;height:169px;background:linear-gradient(180deg,#c3c9cf 0%,#d9d3c6 50%,#4e5a4c 100%)}
.p4{left:165px;top:174px;width:164px;height:251px;background:linear-gradient(180deg,#5d6c93 0%,#c79aa5 25%,#c9c6cc 50%,#5b6664 80%,#2f3a35 100%)}
</style>
</head>
<body>

<section class="spread spread--cover">
  <article class="page page--orange">
    <div class="back-photo" role="img" aria-label="Faded photo of a sculpture, tinted orange"></div>
    <p class="tagline">Real estate in existing and new buildings, visions and solutions– always in tune with the times.</p>
    <div class="tagline-rule"></div>
    <div class="contact">
      <p class="contact-title">KONTAKT</p>
      <p><b>Tel:</b> +49891234567-100</p>
      <p><b>Email:</b> kontakt@blor.de</p>
      <p><b>Web:</b> www.blor.de</p>
      <div class="group">
        <p class="group-title">NEUBAUPROJEKTE</p>
        <p>BLOR Neubau GmbH Gut Lindenhof • Lindenhof 3 85640 Feldkirch</p>
        <p class="group-title" style="margin-top:3px">BESTEHENDE IMMOBILIEN</p>
        <p>BLOR Immobilien GmbH Birkenstr. 118 80805 München</p>
      </div>
    </div>
    <svg class="badge" width="60" height="60" viewBox="0 0 60 60" aria-hidden="true">
      <circle cx="30" cy="30" r="28" fill="none" stroke="#ffffff" stroke-width="1.5"/>
    </svg>
  </article>

  <article class="page page--white">
    <div class="band band--top"></div>
    <p class="brand-name">BLOR</p>
    <div class="bracket"></div>
    <div class="bracket-inner"></div>
    <div class="cover-photo" role="img" aria-label="Photo of a tall residential building with orange balcony frames seen from below against the sky"></div>
    <h1 class="headline"><span class="dark">HERZBLUT</span><br><span class="accent">TRIFFT IMMOBILIEN</span></h1>
    <p class="cover-url">www.blor.de</p>
    <div class="band band--bottom"></div>
  </article>
</section>

<section class="spread spread--inside">
  <article class="page page--white">
    <div class="section-mark" style="top:12px"></div>
    <h2 class="section-title" style="top:21px">OBJEKT</h2>
    <div class="section-rule" style="top:42px;width:64px"></div>
    <p class="body-copy" style="top:54px">Im Stadtteil Schwabing gelegen, gehört dieses im Jahr 1972 erbaute Gebäude zur Münchner Geschichte. Ehemals als Hotel für das Nordpalais geplant, kennt jeder richtige Münchner mindestens eine Person, die hier einmal gewohnt hat. Durch diverse Modernisierungen und Sanierungen in den Jahren von 2012 bis heute ist das Objekt in einem guten, modernen Zustand. Überwiegend 1-Zimmer-Apartments verteilen sich hier auf 15 Etagen. Die helle, vollmöblierte Wohnung besticht durch einen praktisch geschnittenen Grundriss und ist mit einem Laminatboden ausgestattet. Im Flur befindet sich ein geräumiger Einbauschrank der perfekten Stauraum bietet. Der Wohn-/Schlafraum ist mit einem Bett, Esstisch mit Stühlen sowie einer modernen Schrankwand mit TV ausgestattet. Die Ausstattung der kleinen, separaten Küche mit Fliesenboden besteht aus einer Einbauküche mit Kühlschrank und Mikrowelle. Die Wohnung verfügt über ein weiß gefliestes Bad mit Wanne, WC, Waschbecken mit Unterschrank und Decken-Downlights. Der große Balkon, von welchem Sie bis in die späten Abendstunden die Sonne genießen können, lädt zum Verweilen ein. Ebenfalls gehören ein Kellerabteil sowie ein Außenstellplatz zur Wohnung. Die Wohnung ist seit dem 01.10.2022 mit einer Kaltmiete von 975 €/Monat zzgl. einer jährlichen Staffel von 30€ vermietet. Diese Staffel besteht für weitere vier Jahre. Der zugehörige Außenstellplatz ist für 70 €/Monat vermietet.</p>

    <div class="section-mark" style="top:217px"></div>
    <h2 class="section-title" style="top:226px">IMMOBILIE BEWERTEN</h2>
    <div class="section-rule" style="top:247px;width:183px"></div>
    <p class="body-copy" style="top:260px">Sie möchten wissen, wie viel Ihre Immobilie wert ist? Mit der kostenlosen Online-Immobilienbewertung der BLOR erhalten Sie innerhalb weniger Minuten eine erste, realistische Marktpreiseinschätzung für Ihr Objekt – und das für Immobilien in ganz Deutschland. Im Anschluss stehen Ihnen unsere Immobilienexperten für eine fundierte und detaillierte Bewertung vor Ort gerne zur Seite.</p>

    <div class="feature-box">
      <h3 class="feature-col-title" style="left:12px">BESCHREIBUNG</h3>
      <h3 class="feature-col-title" style="left:145px">OBJEKT</h3>
      <ul class="feature-list feature-list--main">
        <li>VOLLMÖBLIERT</li>
        <li>BAD MIT WANNE UND WC</li>
        <li>SEPARATE KÜCHE MIT</li>
        <li class="cont">EINBAUKÜCHE</li>
        <li>GROSSZÜGIGER BALKON</li>
        <li>KELLERRAUM</li>
        <li>WASCHRAUM IM UG</li>
        <li>AUSSENSTELLPLATZ</li>
      </ul>
      <div class="feature-divider"></div>
      <ul class="feature-list feature-list--detail">
        <li>Anschluss an das Fernwärmenetz 2016</li>
        <li>Sukzessiver Fenstertausch der Fenster in den Wohnungen und Fluren/Treppenhaus</li>
        <li>Flursanierung in allen Stockwerken bereits durchgeführt</li>
        <li>Haustechnik: Einbau von Strangventilen, Entfernen von Totleitungen, Einbau einer intelligenten Steuerung der Warmwasserheizung</li>
        <li>Inbetriebnahme der intelligenten Außentemperatur-Steuerung der Heizung zur Betriebskostensenkung</li>
        <li>Sanierung der Gemeinschaftsflächen bereits abgeschlossen</li>
        <li>Waschmaschinenraum im UG mit intelligentem Waschmaschinenbuchungssystem</li>
        <li>Erneuerung der Aufzugstechnik bereits abgeschlossen</li>
        <li>Verlegung von Glasfaser direkt in alle Wohnungen</li>
        <li>Kickbox- und Fitnessstudio mit Mieteinnahmen für die WEG</li>
      </ul>
    </div>
  </article>

  <article class="page page--white">
    <div class="section-mark" style="top:12px"></div>
    <h2 class="section-title" style="top:21px">UNSERE PROJEKTE</h2>
    <div class="section-rule" style="top:42px;width:150px"></div>
    <div class="project-grid">
      <div class="project p1" role="img" aria-label="Rendering of a modern residential block with a playground in the courtyard">
        <span class="project-label">Hausfeld München West</span>
      </div>
      <div class="project p2" role="img" aria-label="Rendering of a white apartment building at dusk">
        <span class="project-label">Referenzen</span>
      </div>
      <div class="project p3" role="img" aria-label="Rendering of a light stone residential building with trees">
        <span class="project-label">Demnächst</span>
      </div>
      <div class="project p4" role="img" aria-label="Rendering of a residential courtyard at sunset">
        <span class="project-label">Lindenbogen Freising</span>
      </div>
    </div>
  </article>
</section>

</body>
</html>
```